I need a complete stationary pack for a real estate office that sells and manages residential proper

We need a stationary design pack for my real estate office called ‘wevaultestate’ that is in Queensland Australia. My offices are both in suburban and coastal locations in the south west corner of Queensland at the Sunshine Coast and Brisbane.
We predominately manage real estate on behalf of owners and sell property in the residential sector.
I have attached a copy of our existing design of my business card and do like the current concept/layout. In saying this you may be able to use this existing theme across to the other items required or see opportunity on how to improve what I have already.
I would like to see concepts for the following products:
- Letterhead
- Fax header
- Business cards
- Email signature
- With complements slips and
- Envelopes
I have attached our current logo that was designed by Artflockly and the font is Prelo.

I am looking for a contemporary design that is professional and reflects trust and professionalism. I am currently using the logo with a black background on some material as per the following link

http://www.plotmarket.example.au/listing/for-sale/house/qld/tarrin/?adid=7305184422&sp=3

I have posted another job 517386 for signage and the company car signage done too if you are interested.

Please do not hesitate to contact me should you have any questions. Thank you.

Target Market(s)

Western speaking people aged from 25 to 60 from modest backgrounds to well off individuals

Industry/Entity Type

Real Estate

Requirements
Must have
• Professional in appearance, show a mature and trustworthy image
Should not have
• As there is good colour with the logo, i am do not want over the top designs or colours

```html
<!DOCTYPE html>
<html lang="en">
<head>
<meta charset="utf-8">
<title>wevaultestate business card</title>
<link href="https://fonts.googleapis.com/css2?family=Open+Sans:wght@400;600;700&display=swap" rel="stylesheet">
<style>
  :root {
    --bg: #e9e5de;
    --card-white: #ffffff;
    --card-black: #0b0b0c;
    --ink: #3b3d4a;
    --red: #e2332b;
    --purple: #7b2f8e;
    --blue: #1f7ac2;
    --green: #2f9e3c;
    --orange: #f39a1e;
    --orange-red: #e8552a;
    --photo-sky: #6f9fc4;
    --photo-suit: #2a3240;
  }
  * { box-sizing: border-box; margin: 0; padding: 0; }
  html, body { width: 1200px; height: 1024px; overflow: hidden; }
  body {
    background: var(--bg);
    font-family: "Open Sans", Arial, sans-serif;
    position: relative;
  }
  .card {
    position: absolute;
    left: 200px;
    width: 800px;
    height: 457px;
    border-radius: 26px;
    overflow: hidden;
    box-shadow: 0 10px 28px rgba(0,0,0,.18);
  }
  .card-front { top: 36px; background: var(--card-white); }
  .card-back { top: 530px; background: var(--card-black); }

  .web-name { color: var(--green); }

  /* front */
  .brand {
    position: absolute;
    left: 70px;
    top: 176px;
    display: flex;
    align-items: center;
    gap: 16px;
  }
  .brand-dot {
    width: 34px; height: 34px; border-radius: 50%;
    background: var(--blue);
    flex: none;
  }
  .brand-name {
    font-size: 46px;
    font-weight: 600;
    color: var(--ink);
    letter-spacing: -0.5px;
    line-height: 1;
  }
  .address {
    position: absolute;
    left: 70px;
    top: 302px;
    font-size: 17px;
    color: var(--ink);
    line-height: 1.6;
  }
  .address-row { display: flex; align-items: center; gap: 8px; }
  .address-row.indent { padding-left: 22px; }
  .photo {
    position: absolute;
    right: 104px;
    top: 34px;
    width: 172px;
    height: 122px;
    background: linear-gradient(180deg, var(--photo-sky) 0%, #9cbfd6 55%, var(--photo-suit) 56%, var(--photo-suit) 100%);
    border: 2px solid #dcdcdc;
  }
  .person {
    position: absolute;
    right: 104px;
    top: 164px;
    text-align: right;
    line-height: 1.2;
  }
  .person-name { color: var(--red); font-weight: 700; font-size: 20px; }
  .person-title { color: var(--blue); font-size: 16px; }
  .contacts {
    position: absolute;
    right: 70px;
    top: 232px;
    font-size: 17px;
    color: var(--ink);
    line-height: 1.7;
  }
  .contact-row { display: flex; justify-content: flex-end; align-items: center; gap: 10px; }
  .icon { width: 14px; height: 14px; flex: none; }
  .colour-band {
    position: absolute;
    left: 0; right: 0; bottom: 0;
    height: 16px;
    display: flex;
    gap: 3px;
    background: var(--card-white);
  }
  .colour-band span { flex: 1; }

  /* back */
  .back-brand {
    position: absolute;
    left: 0; right: 0;
    top: 186px;
    display: flex;
    justify-content: center;
    align-items: center;
    gap: 18px;
  }
  .back-brand .brand-name { color: #ffffff; font-size: 54px; }
  .back-brand .brand-dot { width: 40px; height: 40px; }
  .back-web {
    position: absolute;
    left: 0; right: 0;
    top: 272px;
    text-align: center;
    color: #cfcfcf;
    font-size: 17px;
  }
</style>
</head>
<body>
  <section class="card card-front">
    <div class="photo" role="img" aria-label="Portrait photo of the principal"></div>
    <div class="person">
      <div class="person-name">Darren Kowal</div>
      <div class="person-title">Principal</div>
    </div>

    <div class="contacts">
      <div class="contact-row">
        <span>0412 555 019</span>
        <svg class="icon" viewBox="0 0 14 14"><rect x="3" y="1" width="8" height="12" rx="1.5" fill="none" stroke="#e2332b" stroke-width="1.6"/></svg>
      </div>
      <div class="contact-row">
        <span>07 5550 2146</span>
        <svg class="icon" viewBox="0 0 14 14"><path d="M2 4c0 5 3 8 8 8l2-2-3-2-1 1C6 8 6 7 6 6l1-1-2-3z" fill="#e2332b"/></svg>
      </div>
      <div class="contact-row">
        <span>darren@<span class="web-name">wevaultestate</span>.com.au</span>
        <svg class="icon" viewBox="0 0 14 14"><rect x="1" y="3" width="12" height="8" fill="#e2332b"/><path d="M1 3l6 5 6-5" fill="none" stroke="#fff" stroke-width="1.2"/></svg>
      </div>
    </div>

    <div class="brand">
      <span class="brand-dot"></span>
      <span class="brand-name">wevaultestate</span>
    </div>

    <div class="address">
      <div class="address-row">
        <svg class="icon" viewBox="0 0 14 14"><path d="M7 1a4 4 0 0 0-4 4c0 3 4 8 4 8s4-5 4-8a4 4 0 0 0-4-4z" fill="#e2332b"/><circle cx="7" cy="5" r="1.5" fill="#fff"/></svg>
        <span>shop 4, 212 harbour parade,</span>
      </div>
      <div class="address-row indent"><span>tarrin qld 4571</span></div>
      <div class="address-row">
        <svg class="icon" viewBox="0 0 14 14"><circle cx="7" cy="7" r="6" fill="#e2332b"/><path d="M1 7h12M7 1c-3 3-3 9 0 12M7 1c3 3 3 9 0 12" fill="none" stroke="#fff" stroke-width="1"/></svg>
        <span>www.<span class="web-name">wevaultestate</span>.com.au</span>
      </div>
    </div>

    <div class="colour-band">
      <span style="background:var(--red)"></span>
      <span style="background:var(--purple)"></span>
      <span style="background:var(--blue)"></span>
      <span style="background:var(--green)"></span>
      <span style="background:var(--orange)"></span>
      <span style="background:var(--orange-red)"></span>
    </div>
  </section>

  <section class="card card-back">
    <div class="back-brand">
      <span class="brand-name">wevaultestate</span>
      <span class="brand-dot"></span>
    </div>
    <div class="back-web">www.<span class="web-name">wevaultestate</span>.com.au</div>
  </section>
</body>
</html>
```